Harborline Kidney Services Brochure - Marketing brochure for a dialysis company in the USA

I want a brochure to be created for my business. I have a brochure that can be used as a comparison. My old Company name is Bluewater Renal Infusion Partners. The new Company Name is Harborline Kidney Services. I have a sample of the Old Brochure. and I uploaded the Logo of HKS. It will be used by my sales agents to introduce my company to potential client hospitals.

Target Market(s)

CEOs of Acute Hospitals and Medical Centers

Industry/Entity Type

Health Care

Requirements
Must have
• Use the sample as a guide. This project is for a 4 page brochure. (2 letter size pages folded in half crosswise) Use the text from the old brochure to the new brochure, replacing the old info with the new company info as needed.
Nice to have
• Here is my company info:
• Harborline Kidney Services
• 4180 W 61st Ave
• Suite D
• It will be nice if the designer can give me the project files that would allow me to edit the text of the brochure.
• McAllen, TX 78392
• (956) 417-2863
• admin@HarborlineKidneyLLC.example
• www.harborlinekidney.example

```html
<!DOCTYPE html>
<html lang="en">
<head>
<meta charset="utf-8">
<title>Harborline Kidney Services – Brochure Cover</title>
<link href="https://fonts.googleapis.com/css2?family=Montserrat:wght@600;700&family=Oswald:wght@500;600&family=Roboto+Condensed:ital,wght@1,700&display=swap" rel="stylesheet">
<style>
  :root {
    --page-bg: #e6e7e9;
    --brand-red: #c80a0a;
    --brand-blue: #1c23c8;
    --paper-white: #ffffff;
    --paper-grey: #dcdcdc;
    --logo-blue: #1c28a8;
    --photo-light: #e7edf0;
    --photo-mid: #c9d6dc;
  }
  * { margin: 0; padding: 0; box-sizing: border-box; }
  html, body {
    width: 1200px; height: 828px; overflow: hidden;
    background: var(--page-bg);
  }
  .spread {
    position: absolute; left: 30px; top: 34px;
    width: 1140px; height: 760px;
    display: flex;
    box-shadow: 0 6px 24px rgba(0,0,0,.18);
  }
  .panel { position: relative; width: 570px; height: 760px; overflow: hidden; }
  .panel svg { position: absolute; inset: 0; }
  .back-cover { background: linear-gradient(120deg, var(--paper-grey), var(--paper-white) 55%); }
  .front-cover { background: var(--paper-white); }

  .logo {
    position: absolute; text-align: center; color: var(--logo-blue);
    font-family: "Montserrat", sans-serif; font-weight: 700;
    transform: translateX(-50%);
  }
  .logo__mark { display: block; font-size: 50px; line-height: 1; letter-spacing: 1px; }
  .logo__name { display: block; font-size: 10.5px; letter-spacing: .6px; margin-top: 3px; white-space: nowrap; }
  .back-cover .logo { left: 282px; top: 400px; }
  .front-cover .logo { left: 298px; top: 58px; }

  .call-label {
    position: absolute; left: 0; width: 570px; top: 516px; text-align: center;
    font-family: "Montserrat", sans-serif; font-weight: 600;
    font-size: 32px; letter-spacing: 1px; color: var(--paper-white);
  }
  .call-number {
    position: absolute; left: 0; width: 570px; top: 562px; text-align: center;
    font-family: "Roboto Condensed", sans-serif; font-style: italic; font-weight: 700;
    font-size: 50px; color: var(--paper-white);
  }
  .headline {
    position: absolute; left: 0; width: 570px; top: 540px; text-align: center;
    font-family: "Oswald", sans-serif; color: var(--paper-white); text-transform: uppercase;
  }
  .headline__lead { display: block; font-size: 26px; font-weight: 500; letter-spacing: 1.5px; }
  .headline__main { display: block; font-size: 38px; font-weight: 600; letter-spacing: 1px; line-height: 1.2; }
</style>
</head>
<body>
<main class="spread">
  <section class="panel back-cover">
    <svg viewBox="0 0 570 760" width="570" height="760" aria-hidden="true">
      <path d="M0 420 C180 402 390 395 570 408 L570 422 C390 410 180 416 0 436 Z" fill="var(--brand-blue)"/>
      <path d="M0 452 C180 432 390 425 570 436 L570 760 L0 760 Z" fill="var(--brand-red)"/>
      <ellipse cx="282" cy="432" rx="145" ry="64" fill="var(--paper-white)"/>
    </svg>
    <div class="logo">
      <span class="logo__mark">HKS</span>
      <span class="logo__name">HARBORLINE KIDNEY SERVICES</span>
    </div>
    <p class="call-label">CALL US NOW:</p>
    <p class="call-number">1-888-555-0147</p>
  </section>

  <section class="panel front-cover">
    <svg viewBox="0 0 570 760" width="570" height="760">
      <defs>
        <linearGradient id="ward-fade" x1="0" y1="0" x2="1" y2="1">
          <stop offset="0" stop-color="var(--photo-mid)"/>
          <stop offset="1" stop-color="var(--photo-light)"/>
        </linearGradient>
        <radialGradient id="portrait-tone" cx=".6" cy=".45" r=".7">
          <stop offset="0" stop-color="#f2f1ec"/>
          <stop offset=".6" stop-color="#d8d6cc"/>
          <stop offset="1" stop-color="#b9b3a6"/>
        </radialGradient>
      </defs>
      <rect x="0" y="0" width="570" height="420" fill="url(#ward-fade)" opacity=".55" role="img" aria-label="Faded background photo of a nurse in a hospital dialysis ward"/>
      <rect x="0" y="0" width="570" height="150" fill="var(--paper-white)" opacity=".55"/>
      <path d="M0 408 C180 398 390 410 570 430 L570 444 C390 424 180 412 0 422 Z" fill="var(--brand-blue)"/>
      <path d="M0 436 C180 426 390 440 570 460 L570 760 L0 760 Z" fill="var(--brand-red)"/>
      <circle cx="300" cy="330" r="202" fill="var(--brand-red)"/>
      <circle cx="304" cy="334" r="196" fill="var(--brand-blue)"/>
      <circle cx="304" cy="334" r="190" fill="var(--paper-white)"/>
      <circle cx="304" cy="334" r="180" fill="url(#portrait-tone)" role="img" aria-label="Photo of a smiling doctor with a stethoscope in a dialysis room, a nurse tending a patient behind him"/>
    </svg>
    <div class="logo">
      <span class="logo__mark">HKS</span>
      <span class="logo__name">HARBORLINE KIDNEY SERVICES</span>
    </div>
    <h1 class="headline">
      <span class="headline__lead">Tired of paying outrageous</span>
      <span class="headline__main">Prices for inpatient dialysis?</span>
    </h1>
  </section>
</main>
</body>
</html>
```